Restaurant Menu Design for Meal Prep offered in a food display cooler at a local Gym

I am looking for a menu design with the following items . I would like a workable copy if possible so in the future we can change pricing on this file , or change items . This file will be uploaded on a USB drive and then plugged into a TV. Please ensure a JPEG file is included so this will also work on this TV.

Have a look at our website , www.vantorelkitchen.com for ideas for design that represent the brand appropriately.
The below are the menu items that we would need displayed along with their pricing.

BREAKFAST MEAL PREP ITEMS
Blueberry Pancakes $12.00
Full Throttle Burrito $10.95

LUNCH/DINNER MEAL PREP OPTIONS
BBQ Glazed Salmon $16.50
Cheeseburger Bowl $13.50
Chicken Alfredo $12.00
Pesto Chicken Pasta $12.00
Chicken Parmesan $13.00
Taco Bowl $14.00
Steak Bite and Green Stir Fry $12.00
Asian Chicken Teriyaki $12.00
Galloway Stir Fry $15.95

I will attach our logo below, this will need to be on the design. The "heading" (for example breakfast meal prep items and lunch/dinner meal prep options) for the menu should also be on the design.

Ive attached a couple of photos that you need to add to your design.

Target Market(s)

This will be displayed in a GYM

Industry/Entity Type

Meal Prep + Fitness Industry

Requirements
Must have
• Vantorel Logo and Photos attached
Nice to have
• Maybe incorporate something that represents working out or healthy lifestyle in design without going too overboard

```html
<!DOCTYPE html>
<html lang="en">
<head>
<meta charset="utf-8">
<title>Vantorel Healthy Kitchen – Meal Prep Menu</title>
<link rel="stylesheet" href="https://fonts.googleapis.com/css2?family=Poppins:wght@700;800&family=Open+Sans:wght@700&display=swap">
<style>
  :root {
    --brand-green: #8fbe22;
    --text-grey: #8a8a8a;
    --rule-grey: #7a7a7a;
    --panel: #ffffff;
    --photo-wood: #dfe6ea;
    --photo-pancake: #e8c48e;
    --photo-pasta: #b7a36a;
  }
  * { margin: 0; padding: 0; box-sizing: border-box; }
  html, body { width: 1200px; height: 1200px; overflow: hidden; }
  body { background: var(--brand-green); position: relative; }

  .menu-panel {
    position: absolute; left: 211px; top: 55px;
    width: 778px; height: 1090px;
    background: var(--panel); overflow: hidden;
  }
  .hero-art { position: absolute; left: 0; top: 0; }

  .brand {
    position: absolute; left: 419px; top: 62px; width: 318px;
    text-align: right;
  }
  .brand-name {
    font-family: "Poppins", sans-serif; font-weight: 800;
    font-size: 58px; line-height: 1; letter-spacing: 1px;
    color: var(--text-grey); text-transform: uppercase;
  }
  .brand-tagline {
    margin-top: 6px;
    font-family: "Poppins", sans-serif; font-weight: 700;
    font-size: 18.5px; color: var(--brand-green); letter-spacing: -0.2px;
    white-space: nowrap;
  }
  .brand-tagline .divider { margin: 0 10px; font-weight: 400; }

  .menu-title {
    position: absolute; left: 0; top: 525px; width: 100%;
    text-align: center;
    font-family: "Poppins", sans-serif; font-weight: 800;
    font-size: 32px; line-height: 40px; letter-spacing: 0.2px;
  }
  .menu-title .line-green { color: var(--brand-green); display: block; }
  .menu-title .line-grey { color: var(--text-grey); display: block; }

  .menu-section { position: absolute; font-family: "Open Sans", sans-serif; font-weight: 700; }
  .section-heading {
    font-size: 18.5px; color: var(--brand-green); line-height: 24px;
    margin-bottom: 5px; white-space: nowrap;
  }
  .item-list {
    list-style: none;
    border: 1px dashed var(--brand-green);
    padding: 0 16px 0 10px;
  }
  .item-list li {
    font-size: 18.5px; color: var(--text-grey);
    height: 39px; line-height: 39px; white-space: nowrap;
    border-bottom: 1px dashed var(--brand-green);
  }
  .item-list li:last-child { border-bottom: none; }

  .section-breakfast { left: 52px; top: 661px; width: 293px; }
  .section-breakfast .item-list { padding-top: 4px; padding-bottom: 4px; }
  .section-breakfast .item-list li { height: 44px; line-height: 44px; }

  .section-main { left: 381px; top: 661px; width: 346px; }
  .section-main .item-list { padding-bottom: 14px; }
</style>
</head>
<body>
  <main class="menu-panel">
    <svg class="hero-art" width="778" height="500" viewBox="0 0 778 500">
      <defs>
        <linearGradient id="pancakeTone" x1="0" y1="0" x2="1" y2="1">
          <stop offset="0" stop-color="#e4ebee"/>
          <stop offset="0.5" stop-color="#e8c48e"/>
          <stop offset="1" stop-color="#d6dde2"/>
        </linearGradient>
        <linearGradient id="pastaTone" x1="0" y1="0" x2="0" y2="1">
          <stop offset="0" stop-color="#e4ebee"/>
          <stop offset="0.55" stop-color="#b7a36a"/>
          <stop offset="1" stop-color="#e9eef0"/>
        </linearGradient>
      </defs>
      <circle cx="163" cy="190" r="262" fill="none" stroke="var(--brand-green)" stroke-width="2" stroke-dasharray="7 5"/>
      <circle cx="163" cy="190" r="255" fill="url(#pancakeTone)" role="img" aria-label="Photo of stacked blueberry pancakes with yogurt drizzle on a white plate"/>
      <circle cx="378" cy="296" r="150" fill="var(--panel)"/>
      <circle cx="378" cy="296" r="143" fill="none" stroke="var(--rule-grey)" stroke-width="1.5" stroke-dasharray="5 4"/>
      <circle cx="378" cy="296" r="137" fill="url(#pastaTone)" role="img" aria-label="Photo of pesto chicken pasta with broccoli in a white bowl"/>
    </svg>

    <header class="brand">
      <div class="brand-name">Vantorel</div>
      <div class="brand-tagline">HEALTHY KITCHEN<span class="divider">|</span>MEAL PREP</div>
    </header>

    <h1 class="menu-title">
      <span class="line-green">BREAKFAST MEAL PREP ITEMS AND</span>
      <span class="line-grey">LUNCH/DINNER MEAL PREP OPTIONS</span>
    </h1>

    <section class="menu-section section-breakfast">
      <h2 class="section-heading">BREAKFAST MEAL PREP ITEMS</h2>
      <ul class="item-list">
        <li>Blueberry Pancakes $12.00</li>
        <li>Full Throttle Burrito $10.95</li>
      </ul>
    </section>

    <section class="menu-section section-main">
      <h2 class="section-heading">LUNCH/DINNER MEAL PREP OPTIONS</h2>
      <ul class="item-list">
        <li>BBQ Glazed Salmon $16.50</li>
        <li>Cheeseburger Bowl $13.50</li>
        <li>Chicken Alfredo $12.00</li>
        <li>Pesto Chicken Pasta $12.00</li>
        <li>Chicken Parmesan $13.00</li>
        <li>Taco Bowl $14.00</li>
        <li>Steak Bite and Green Stir Fry $12.00</li>
        <li>Asian Chicken Teriyaki $12.00</li>
        <li>Galloway Stir Fry $15.95</li>
      </ul>
    </section>
  </main>
</body>
</html>
```